Bright Tooth Dentistry Business Card

We need business cards for our dental office.
We are looking for a clean, elegant design

We provide dental services to children.
Our card needs to be appealing to referring dentists, parents and our team

Target Market(s)

referring dentists, parents and our team

Industry/Entity Type

Dental Clinic

Contact Information for Business Card

4816 Juniper Lane, Suite 100
Fairview Crest, PA 15237

412-837-2961 Voice
412-837-2962 fax
info@brighttoothdentalpa.com email
www.brighttoothdentalpa.com web

Font styles to use
Sans Serif

Requirements
Must have
• White background - clean, crisp, elegant, simple
• rounded corners
• different color palate - once we come up with design, we will replace the blue with orange, green,
Nice to have
• Follow our logo typeface and colors
• then we can replace color

```html
<!DOCTYPE html>
<html lang="en">
<head>
<meta charset="utf-8">
<title>Bright Tooth Dentistry – Business Card</title>
<link href="https://fonts.googleapis.com/css2?family=Source+Sans+3:wght@400;600&display=swap" rel="stylesheet">
<style>
  :root {
    --brand: #00aeef;
    --paper: #ffffff;
    --ink: #1a1a1a;
    --edge: #e2e2e2;
    --shadow: rgba(0, 0, 0, 0.28);
  }
  * { margin: 0; padding: 0; box-sizing: border-box; }
  html, body {
    width: 1200px; height: 960px; overflow: hidden;
    background: var(--paper);
    font-family: "Source Sans 3", "Source Sans Pro", sans-serif;
  }
  .card {
    position: absolute;
    left: 286px; width: 629px; height: 359px;
    border-radius: 26px;
    box-shadow: 0 2px 4px var(--shadow);
  }
  .card-front { top: 109px; background: var(--brand); }
  .card-back  { top: 492px; background: var(--paper); border: 1px solid var(--edge); }
  .card-inner {
    position: absolute;
    left: 21px; top: 22px; width: 585px; height: 315px;
    border-radius: 24px;
  }
  .card-front .card-inner { background: var(--paper); }
  .card-back .card-inner { background: var(--brand); }

  .brand-mark {
    position: absolute;
    width: 44px; height: 44px; border-radius: 50%;
  }
  .brand-name {
    position: absolute;
    font-weight: 600;
    font-size: 33px;
    line-height: 1;
    white-space: nowrap;
  }
  .card-front .brand-mark { left: 189px; top: 18px; background: var(--brand); }
  .card-front .brand-name { left: 89px; top: 91px; color: var(--brand); }
  .card-back .brand-mark { left: 270px; top: 108px; background: var(--paper); }
  .card-back .brand-name { left: 0; width: 585px; text-align: center; top: 178px; color: var(--paper); }

  .address, .contact-list {
    position: absolute; left: 89px;
    font-size: 17px; color: var(--ink);
  }
  .address { top: 143px; line-height: 26.5px; }
  .contact-list { top: 206px; list-style: none; line-height: 26.2px; }
  .contact-list li { display: flex; }
  .contact-label { color: var(--brand); width: 20px; }
  .contact-sep { width: 8px; }
</style>
</head>
<body>
  <section class="card card-front">
    <div class="card-inner">
      <span class="brand-mark" aria-hidden="true"></span>
      <span class="brand-name">Bright Tooth Dentistry</span>
      <p class="address">4816 Juniper Lane, Suite 240<br>Fairview Crest, PA 15237</p>
      <ul class="contact-list">
        <li><span class="contact-label">P</span><span class="contact-sep">:</span><span>412-837-2961</span></li>
        <li><span class="contact-label">F</span><span class="contact-sep">:</span><span>412-837-2962</span></li>
        <li><span class="contact-label">E</span><span class="contact-sep">:</span><span>info@brighttoothdentalpa.com</span></li>
        <li><span class="contact-label">W</span><span class="contact-sep">:</span><span>www.brighttoothdentalpa.com</span></li>
      </ul>
    </div>
  </section>

  <section class="card card-back">
    <div class="card-inner">
      <span class="brand-mark" aria-hidden="true"></span>
      <span class="brand-name">Bright Tooth Dentistry</span>
    </div>
  </section>
</body>
</html>
```